We are looking for a simple design that would be uplifting for
upscale drug addicts

MERIDIAN CIRCLE

PLEASE SEE THE LINK FOR TAG LINE AND CONTENT

thank you.

here is all the actual info we need and we want something like this...

http://assets.qlm.brivostore.com/rest/items/7c2910e5b337de81f94a02bd57e644163ab9fe0a6712?uid=bd31c9e2f7a04c18b6e0d44721fa93c5%2fdrafts&expires=1408211537&signature=kTp4WmQxNvLzHa8YbEoRcJsGf2B%3d

The shape and colors don't have to be like what I posted it is only an example.

Target Market(s)

Wall Street, internet and creative types, men, early 30's,
upwardly mobile, drug addicts

current site

bkltornavel.com

now launching new name Meridian Circle

Industry/Entity Type

Drug

Requirements
Must have
• upscale look, great font
Should not have
• a corporate look but should not look like a clinic.

```html
<!DOCTYPE html>
<html lang="en">
<head>
<meta charset="utf-8">
<title>Meridian Circle — Owen Halbrook</title>
<link href="https://fonts.googleapis.com/css2?family=Bebas+Neue&family=Montserrat:wght@700;800&display=swap" rel="stylesheet">
<style>
  :root {
    --ink: #000000;
    --paper: #ffffff;
    --gutter: 62px;
    --measure: 542px;
  }
  * { margin: 0; padding: 0; box-sizing: border-box; }
  html, body {
    width: 667px;
    height: 1200px;
    overflow: hidden;
    background: var(--ink);
  }
  .card {
    position: relative;
    width: 667px;
    height: 1200px;
    background: var(--ink);
    color: var(--paper);
    font-family: "Montserrat", Arial, sans-serif;
    font-weight: 700;
    text-transform: uppercase;
  }
  .line {
    position: absolute;
    left: var(--gutter);
    width: var(--measure);
    display: flex;
    justify-content: space-between;
    align-items: center;
    line-height: 1;
    white-space: nowrap;
  }
  .rule {
    position: absolute;
    left: var(--gutter);
    width: var(--measure);
    height: 5px;
    background: var(--paper);
  }

  /* tagline */
  .tagline { font-size: 29px; height: 24px; }
  .tagline--one { top: 58px; }
  .tagline--two { top: 96px; }
  .tagline--three { top: 152px; font-size: 27px; }
  .rule--top { top: 194px; }

  /* wordmark */
  .wordmark {
    font-family: "Bebas Neue", "Arial Narrow", sans-serif;
    font-weight: 400;
    font-size: 154px;
    height: 110px;
  }
  .wordmark--one { top: 222px; }
  .wordmark--two { top: 366px; }
  .wordmark--three { top: 507px; }
  .rule--bottom { top: 653px; }

  /* contact */
  .name { top: 698px; font-size: 50px; height: 38px; font-weight: 800; }
  .role { top: 759px; font-size: 33px; height: 26px; }
  .street { top: 799px; font-size: 32px; height: 26px; }
  .city { top: 840px; font-size: 32px; height: 26px; }
  .phone { top: 880px; font-size: 37px; height: 30px; }
  .email {
    top: 922px;
    font-size: 20px;
    height: 20px;
    justify-content: flex-start;
    letter-spacing: 2.2px;
  }
</style>
</head>
<body>
  <main class="card">
    <p class="line tagline tagline--one"><span>We</span><span>Dont</span><span>Cut</span><span>Any</span><span>Corners</span></p>
    <p class="line tagline tagline--two"><span>When</span><span>It</span><span>Comes</span><span>To</span><span>Your</span></p>
    <p class="line tagline tagline--three"><span>L</span><span>O</span><span>N</span><span>G</span><span>T</span><span>E</span><span>R</span><span>M</span><span>&nbsp;</span><span>R</span><span>E</span><span>C</span><span>O</span><span>V</span><span>E</span><span>R</span><span>Y</span></p>
    <div class="rule rule--top"></div>

    <h1 class="wordmark-block" aria-label="Meridian Circle">
      <span class="line wordmark wordmark--one" aria-hidden="true"><span>M</span><span>E</span><span>R</span><span>I</span></span>
      <span class="line wordmark wordmark--two" aria-hidden="true"><span>D</span><span>I</span><span>A</span><span>N</span></span>
      <span class="line wordmark wordmark--three" aria-hidden="true"><span>C</span><span>I</span><span>R</span><span>C</span><span>L</span><span>E</span></span>
    </h1>
    <div class="rule rule--bottom"></div>

    <p class="line name"><span>Owen</span><span>Halbrook</span></p>
    <p class="line role"><span>Program</span><span>Coordinator</span></p>
    <p class="line street"><span>418</span><span>W.</span><span>52nd</span><span>St.</span><span>Suite</span><span>305</span></p>
    <p class="line city"><span>N</span><span>E</span><span>W</span><span>&nbsp;</span><span>Y</span><span>O</span><span>R</span><span>K</span><span>,</span><span>&nbsp;</span><span>N</span><span>Y</span><span>&nbsp;</span><span>1</span><span>0</span><span>0</span><span>1</span><span>9</span></p>
    <p class="line phone"><span>2</span><span>1</span><span>2</span><span>.</span><span>5</span><span>5</span><span>5</span><span>.</span><span>0</span><span>1</span><span>4</span><span>7</span></p>
    <p class="line email">counselor@meridiancirclenyc.com</p>
  </main>
</body>
</html>
```